Copper Lantern Gatherings need a stand out marketing flyer.

Copper Lantern Gatherings is a company that runs empowerment retreats and bespoke corporate training in creating positive change.
We would like an A5 flyer that is 2 sided. the reverse side of the flyer we would like some of our testimonial quotes.

The flyer should be punchy and not too heavy with wordy detail but have enough detail so people can see what we offer. Encouraging people to contact us to find out more

Our empowerment retreats help people to live without limits, be fierce and wild, be creative and courageous, be fearless and free.
Leave behind
- lack of self esteem
- lack of personal power
- lack of focus
- old fears and beliefs
- overwhelm
Find new
- confidence
- personal empowerment
- commitment
- courage
- resilience

Contact details:
website: www.copperlanterngatherings.example.co.uk
email: info@copperlanterngatherings.example.com
Rebecca Thornby Tel: 07700 900 318
Joanna Pelling Tel: 07700 900 752

You can use as much of the detail above in your design as you would like..
I attach our logos. you can pick which ever design you prefer to work with. I have also attached a file that contains the testimonials for the reverse of the slide. I've also attached a few pictures but these aren't necessary in your design they are just an option/idea for you to consider. You can use alternative pictures should you wish to.

Details for our up and coming events can be found on our website

```html
<!DOCTYPE html>
<html lang="en">
<head>
<meta charset="utf-8">
<title>Copper Lantern Gatherings – A5 Flyer</title>
<link href="https://fonts.googleapis.com/css2?family=Montserrat:wght@500;600&family=Open+Sans:wght@300;400;600&display=swap" rel="stylesheet">
<style>
  :root{
    --bg:#e6e7ea;
    --paper:#ffffff;
    --ink:#2f3032;
    --ink-soft:#6d6f73;
    --dark:#3b3c3f;
    --blue:#0a8fd8;
    --blue-deep:#1a3f9c;
    --blue-light:#29a9ee;
    --tile:#ececed;
    --tile-text:#77797d;
  }
  *{box-sizing:border-box;margin:0;padding:0}
  html,body{width:1200px;height:900px;overflow:hidden}
  body{background:var(--bg);font-family:"Open Sans",Arial,sans-serif;color:var(--ink);position:relative}

  .flyer{position:absolute;top:150px;width:424px;height:600px;background:var(--paper);overflow:hidden;box-shadow:0 10px 28px rgba(0,0,0,.18)}
  .flyer--front{left:146px}
  .flyer--back{left:630px}

  .hero{position:absolute;left:0;top:0;width:424px;height:256px;overflow:hidden}
  .hero__photo{position:absolute;inset:0}
  .flyer--front .hero__photo{background:linear-gradient(160deg,#cfe6ea 0%,#d9d2c4 55%,#e2c9a4 100%)}
  .flyer--back .hero{height:240px}
  .flyer--back .hero__photo{background:linear-gradient(180deg,#8d8e90 0%,#b3b3b4 60%,#c9c9ca 100%)}
  .hero__shapes{position:absolute;inset:0;width:100%;height:100%}

  .brand{position:absolute;display:flex;align-items:center;gap:6px;font-weight:600;font-size:11px;line-height:1.2;color:var(--blue-deep);width:120px}
  .brand__dot{flex:none;width:14px;height:14px;border-radius:50%;background:var(--blue-deep)}
  .flyer--front .brand{left:20px;top:30px}
  .flyer--back .brand{right:16px;top:22px;width:108px}

  .intro{position:absolute;left:0;top:262px;width:100%;text-align:center;padding:0 14px}
  .intro__title{font-family:"Montserrat",Arial,sans-serif;font-weight:600;font-size:10.8px;white-space:nowrap;color:var(--ink);text-transform:uppercase}
  .intro__text{margin-top:8px;padding:0 12px;font-weight:300;font-size:11.5px;line-height:1.45;color:var(--ink)}

  .offer{position:absolute;left:0;top:336px;width:100%;height:146px;background:var(--dark);display:flex;padding:18px 30px 0 34px;gap:34px}
  .offer__col{flex:1}
  .offer__heading{font-weight:300;font-size:12px;color:var(--blue-light);text-transform:uppercase;margin-bottom:5px}
  .offer__list{list-style:none}
  .offer__item{display:flex;align-items:center;gap:8px;font-weight:300;font-size:12px;line-height:1.55;color:#fff}
  .offer__icon{flex:none;width:9px;height:9px}

  .contact{position:absolute;left:0;top:482px;width:100%;height:74px;text-align:center;background:linear-gradient(180deg,#f4f4f5 0%,#fff 60%)}
  .contact__notch{position:absolute;left:50%;top:-1px;transform:translateX(-50%)}
  .contact__title{margin-top:10px;font-family:"Montserrat",Arial,sans-serif;font-weight:600;font-size:14px;line-height:18px;color:var(--ink);text-transform:uppercase}
  .contact__lines{margin-top:3px;font-weight:300;font-size:10.5px;line-height:1.35;color:var(--ink)}

  .footer{position:absolute;left:0;bottom:0;width:100%;height:44px}
  .footer__shapes{position:absolute;inset:0;width:100%;height:100%}
  .footer__url{position:absolute;right:20px;bottom:7px;font-weight:300;font-size:11.5px;color:#fff}

  .testimonials{position:absolute;left:0;top:256px;width:100%;text-align:center}
  .testimonials__title{font-family:"Montserrat",Arial,sans-serif;font-weight:600;font-size:15px;color:var(--ink);text-transform:uppercase}
  .testimonials__sub{font-weight:300;font-size:13px;color:var(--ink-soft);margin-top:2px}
  .quotes{position:absolute;left:14px;top:306px;width:396px;display:grid;grid-template-columns:repeat(3,1fr);gap:8px}
  .quote{background:var(--tile);height:112px;display:flex;align-items:center;justify-content:center;padding:4px 6px;text-align:center;font-weight:300;font-size:9.4px;line-height:1.35;color:var(--tile-text)}
</style>
</head>
<body>

<section class="flyer flyer--front">
  <div class="hero">
    <div class="hero__photo" role="img" aria-label="Photo: a hand holding a large key towards a seated wooden artist's figure with a keyhole in its chest, titled unlock your potential"></div>
    <svg class="hero__shapes" viewBox="0 0 424 256" preserveAspectRatio="none" aria-hidden="true">
      <defs>
        <linearGradient id="frontBlue" x1="0" y1="0" x2="1" y2="1">
          <stop offset="0" stop-color="#29a9ee"/><stop offset="1" stop-color="#1a3f9c"/>
        </linearGradient>
      </defs>
      <polygon points="0,0 215,0 0,172" fill="#fff"/>
      <polygon points="0,112 112,178 0,232" fill="url(#frontBlue)"/>
      <polygon points="0,198 175,256 0,256" fill="#3b3c3f"/>
      <polygon points="424,90 424,214 322,178" fill="url(#frontBlue)"/>
      <polygon points="424,188 424,256 300,256" fill="#fff"/>
    </svg>
    <div class="brand"><span class="brand__dot"></span>Copper Lantern Gatherings</div>
  </div>

  <div class="intro">
    <h1 class="intro__title">Empowerment retreats and bespoke corporate training</h1>
    <p class="intro__text">Our empowerment retreats help people to live without limits, be fierce and wild, be creative and courageous, be fearless and free.</p>
  </div>

  <div class="offer">
    <div class="offer__col">
      <h2 class="offer__heading">Leave behind</h2>
      <ul class="offer__list">
        <li class="offer__item"><svg class="offer__icon" viewBox="0 0 10 10"><circle cx="5" cy="5" r="4.2" fill="none" stroke="#29a9ee" stroke-width="1"/><path d="M4 3l2 2-2 2" fill="none" stroke="#29a9ee" stroke-width="1"/></svg>lack of self esteem</li>
        <li class="offer__item"><svg class="offer__icon" viewBox="0 0 10 10"><circle cx="5" cy="5" r="4.2" fill="none" stroke="#29a9ee" stroke-width="1"/><path d="M4 3l2 2-2 2" fill="none" stroke="#29a9ee" stroke-width="1"/></svg>lack of personal power</li>
        <li class="offer__item"><svg class="offer__icon" viewBox="0 0 10 10"><circle cx="5" cy="5" r="4.2" fill="none" stroke="#29a9ee" stroke-width="1"/><path d="M4 3l2 2-2 2" fill="none" stroke="#29a9ee" stroke-width="1"/></svg>lack of focus</li>
        <li class="offer__item"><svg class="offer__icon" viewBox="0 0 10 10"><circle cx="5" cy="5" r="4.2" fill="none" stroke="#29a9ee" stroke-width="1"/><path d="M4 3l2 2-2 2" fill="none" stroke="#29a9ee" stroke-width="1"/></svg>old fears and beliefs</li>
        <li class="offer__item"><svg class="offer__icon" viewBox="0 0 10 10"><circle cx="5" cy="5" r="4.2" fill="none" stroke="#29a9ee" stroke-width="1"/><path d="M4 3l2 2-2 2" fill="none" stroke="#29a9ee" stroke-width="1"/></svg>overwhelm</li>
      </ul>
    </div>
    <div class="offer__col">
      <h2 class="offer__heading">Find new</h2>
      <ul class="offer__list">
        <li class="offer__item"><svg class="offer__icon" viewBox="0 0 10 10"><circle cx="5" cy="5" r="4.2" fill="none" stroke="#29a9ee" stroke-width="1"/><path d="M4 3l2 2-2 2" fill="none" stroke="#29a9ee" stroke-width="1"/></svg>confidence</li>
        <li class="offer__item"><svg class="offer__icon" viewBox="0 0 10 10"><circle cx="5" cy="5" r="4.2" fill="none" stroke="#29a9ee" stroke-width="1"/><path d="M4 3l2 2-2 2" fill="none" stroke="#29a9ee" stroke-width="1"/></svg>personal empowerment</li>
        <li class="offer__item"><svg class="offer__icon" viewBox="0 0 10 10"><circle cx="5" cy="5" r="4.2" fill="none" stroke="#29a9ee" stroke-width="1"/><path d="M4 3l2 2-2 2" fill="none" stroke="#29a9ee" stroke-width="1"/></svg>commitment</li>
        <li class="offer__item"><svg class="offer__icon" viewBox="0 0 10 10"><circle cx="5" cy="5" r="4.2" fill="none" stroke="#29a9ee" stroke-width="1"/><path d="M4 3l2 2-2 2" fill="none" stroke="#29a9ee" stroke-width="1"/></svg>courage</li>
        <li class="offer__item"><svg class="offer__icon" viewBox="0 0 10 10"><circle cx="5" cy="5" r="4.2" fill="none" stroke="#29a9ee" stroke-width="1"/><path d="M4 3l2 2-2 2" fill="none" stroke="#29a9ee" stroke-width="1"/></svg>resilience</li>
      </ul>
    </div>
  </div>

  <div class="contact">
    <svg class="contact__notch" width="24" height="10" viewBox="0 0 24 10" aria-hidden="true"><polygon points="0,0 24,0 12,10" fill="#3b3c3f"/></svg>
    <h2 class="contact__title">Contact us to find out more</h2>
    <p class="contact__lines">Rebecca Thornby p: 07700 900 318<br>Joanna Pelling p: 07700 900 752<br>info@copperlanterngatherings.example.com</p>
  </div>

  <div class="footer">
    <svg class="footer__shapes" viewBox="0 0 424 44" preserveAspectRatio="none" aria-hidden="true">
      <defs>
        <linearGradient id="frontBand" x1="0" y1="0" x2="1" y2="0">
          <stop offset="0" stop-color="#29a9ee"/><stop offset="1" stop-color="#1a3f9c"/>
        </linearGradient>
      </defs>
      <polygon points="70,44 150,18 424,10 424,44" fill="url(#frontBand)"/>
      <polygon points="0,44 40,8 112,44" fill="#3b3c3f"/>
    </svg>
    <span class="footer__url">www.copperlanterngatherings.example.co.uk</span>
  </div>
</section>

<section class="flyer flyer--back">
  <div class="hero">
    <div class="hero__photo" role="img" aria-label="Photo: a hand labelled fear holding the strings of a running wooden artist's figure like a puppet"></div>
    <svg class="hero__shapes" viewBox="0 0 424 240" preserveAspectRatio="none" aria-hidden="true">
      <defs>
        <linearGradient id="backBlue" x1="0" y1="0" x2="1" y2="1">
          <stop offset="0" stop-color="#29a9ee"/><stop offset="1" stop-color="#1a3f9c"/>
        </linearGradient>
      </defs>
      <polygon points="262,0 424,0 424,118" fill="#fff"/>
      <polygon points="424,60 424,200 360,120" fill="url(#backBlue)"/>
      <polygon points="424,150 424,240 300,240" fill="#3b3c3f"/>
    </svg>
    <div class="brand"><span class="brand__dot"></span>Copper Lantern Gatherings</div>
  </div>

  <div class="testimonials">
    <h1 class="testimonials__title">Testimonial quotes</h1>
    <p class="testimonials__sub">Copper Lantern Gatherings</p>
  </div>

  <div class="quotes">
    <p class="quote">Do not hesitate, just book it! It will transform and enhance your life.</p>
    <p class="quote">If you have a chance to do it then do it, it's one of the best experience of my life.</p>
    <p class="quote">The most wonderful weekend of self-discovery and would recommend it to everyone.</p>
    <p class="quote">I've met the most amazing people and feel like I am well equipped with the tools now to help myself physically and mentally. The best self-care I've ever invested in.</p>
    <p class="quote">It's changed my life, given me perspective and time to develop myself. I've met the most amazing people and learnt so much. It's worth every penny.</p>
    <p class="quote">I can't thank Copper Lantern enough for the tools they have metaphorically equipped me with. They are amazing at what they do.</p>
  </div>

  <div class="footer">
    <svg class="footer__shapes" viewBox="0 0 424 44" preserveAspectRatio="none" aria-hidden="true">
      <defs>
        <linearGradient id="backBand" x1="0" y1="0" x2="1" y2="0">
          <stop offset="0" stop-color="#29a9ee"/><stop offset="1" stop-color="#1a3f9c"/>
        </linearGradient>
      </defs>
      <polygon points="70,44 150,18 424,10 424,44" fill="url(#backBand)"/>
      <polygon points="0,44 40,8 112,44" fill="#3b3c3f"/>
    </svg>
    <span class="footer__url">www.copperlanterngatherings.example.co.uk</span>
  </div>
</section>

</body>
</html>
```